Creation of an elegant and modern turnkey Shopify website

Hello,

We are a new company specializing in the sale of above-ground pools. We want to create a turnkey website, ideally using Shopify. For now, we need a "showcase" site, not an e-commerce platform, with four tabs:

Home Page (an overall presentation of the company)
Our Products (an overview of all the above-ground pools we sell)
Our Projects (a page inspired by Instagram to showcase photos of our future projects)
Contact (a page with all our contact information and a contact form)

We are looking to create a highly visual, elegant, and modern website with vibrant splashes of color. We will provide the text, photos (along with instructions on where to place them on each page), and all other necessary information as attachments.

Thank you in advance for your proposals!

The Brisa Lagoon Team

Target Market(s)

Targeted at Swiss customers (a translator will need to be installed for different languages)

Industry/Entity Type

Sale of customised above-ground pools

Coding

Coded - Design and coding required

Font styles to use
Sans Serif

Colors
0094D4
00A9DD
6FCCEA
C7EBF8
E9F6FB
00AB8E
00BBA5
67D7C9
C6EFE9
E9F9F6

Requirements
Must have
• A stunning, elegant and modern look
Nice to have
• Inspiration from the colors of our logo throughout the site, but in an elegant way
Should not have
• An overly classic look for swimming pool sites

```html
<!DOCTYPE html>
<html lang="en">
<head>
<meta charset="utf-8">
<title>Brisa Lagoon – Above-Ground Pools</title>
<link rel="stylesheet" href="https://fonts.googleapis.com/css2?family=Josefin+Sans:wght@300;400;600&family=Tinos&display=swap">
<style>
  :root{
    --blue:#0094D4;
    --blue-light:#00A9DD;
    --sky:#6FCCEA;
    --green:#00AB8E;
    --teal:#00BBA5;
    --ink:#1b1b1b;
    --grey:#555;
    --bar:#ececec;
    --white:#ffffff;
  }
  *{margin:0;padding:0;box-sizing:border-box}
  html,body{width:1200px;height:5195px;overflow:hidden;background:var(--white)}
  body{position:relative;font-family:"Josefin Sans",sans-serif;color:var(--ink)}
  .abs{position:absolute}

  /* header */
  .call{left:111px;top:32px;font-size:14px;color:var(--grey);font-weight:300;display:flex;align-items:center;gap:5px}
  .brand{left:400px;width:400px;top:52px;text-align:center;font-weight:400;color:var(--blue-light);font-size:30px;line-height:1}
  .tools{left:990px;top:30px;display:flex;gap:18px}
  .nav{top:127px;left:0;width:1200px;display:flex;justify-content:center;gap:52px;font-size:14px;color:var(--grey);font-weight:300}
  .page-title{top:172px;left:0;width:1200px;text-align:center;font-size:56px;font-weight:400;color:var(--ink)}
  .page-title span{color:var(--blue-light)}

  /* hero */
  .hero{left:111px;top:246px;width:978px;height:405px;background:linear-gradient(135deg,#d89a6a,#3fb6d6 45%,#1f8fb8 70%,#c8a27a)}
  .hero-bar{left:111px;top:651px;width:978px;height:45px;background:var(--bar);display:flex;align-items:center;justify-content:center;gap:8px}
  .dot{width:16px;height:16px;border:2px solid #222;border-radius:50%}
  .dot.on{background:#222}

  /* tiles */
  .tile{color:var(--white);padding:0 44px}
  .tile h2{font-size:40px;font-weight:400;line-height:1.3;margin-bottom:18px}
  .tile p{font-size:18px;font-weight:300;line-height:1.68}
  .blue{background:var(--blue)}
  .green{background:var(--green)}

  /* why choose */
  .why{left:0;top:1735px;width:1200px;height:1676px;background:linear-gradient(180deg,var(--blue) 0%,var(--green) 100%)}
  .why h2{position:absolute;top:92px;left:0;width:1200px;text-align:center;color:var(--white);font-weight:400;font-size:40px;line-height:1.3}
  .card{width:478px}
  .card .pic{height:363px}
  .card .label{margin-top:22px;text-align:center;color:var(--white);font-size:29px;font-weight:400;letter-spacing:1px;display:flex;justify-content:center;align-items:center;gap:10px}

  /* footer */
  .footer{left:0;top:4605px;width:1200px;height:590px;background:var(--blue);color:var(--white)}
  .footer .brand-foot{position:absolute;top:130px;left:0;width:1200px;text-align:center;font-size:52px;font-weight:400;line-height:1}
  .subscribe{position:absolute;top:262px;left:0;width:1200px;text-align:center;font-size:31px;font-weight:300}
  .email{position:absolute;left:319px;top:341px;width:562px;height:72px;border:2px solid var(--white);display:flex;align-items:center;justify-content:space-between;padding:0 22px;font-size:24px;font-weight:300}
  .rule{position:absolute;left:0;top:478px;width:1200px;height:1px;background:rgba(255,255,255,.45)}
  .copy{position:absolute;top:514px;left:0;width:1200px;text-align:center;font-family:"Tinos",serif;font-size:24px}
  .btn{background:var(--white);color:var(--ink);font-size:16px;font-weight:600;padding:18px 24px 14px;display:inline-block;margin-top:22px}
</style>
</head>
<body>

<header>
  <div class="abs call">
    <svg width="12" height="12" viewBox="0 0 24 24"><path fill="#555" d="M6.6 10.8a15 15 0 0 0 6.6 6.6l2.2-2.2a1 1 0 0 1 1-.25 11.4 11.4 0 0 0 3.6.57 1 1 0 0 1 1 1V20a1 1 0 0 1-1 1A17 17 0 0 1 3 4a1 1 0 0 1 1-1h3.5a1 1 0 0 1 1 1c0 1.25.2 2.45.57 3.57a1 1 0 0 1-.25 1z"/></svg>
    Call : 555-014-2290
  </div>
  <div class="abs brand">Brisa Lagoon</div>
  <div class="abs tools">
    <svg width="14" height="14" viewBox="0 0 24 24"><circle cx="12" cy="7" r="5" fill="#111"/><path d="M2 23c0-6 4.5-9 10-9s10 3 10 9z" fill="#111"/></svg>
    <svg width="16" height="14" viewBox="0 0 24 22"><path d="M0 1h4l3 13h13l3-9H6" fill="none" stroke="#111" stroke-width="3"/><circle cx="9" cy="19" r="2.3" fill="#111"/><circle cx="19" cy="19" r="2.3" fill="#111"/></svg>
    <svg width="14" height="14" viewBox="0 0 24 24"><rect x="2" y="2" width="20" height="20" fill="none" stroke="#111" stroke-width="3"/><path d="M7 8h10M12 8v10" stroke="#111" stroke-width="3"/></svg>
  </div>
  <nav class="abs nav"><span>Home</span><span>Our Products</span><span>Our Projects</span><span>Contact</span></nav>
  <h1 class="abs page-title">Welcome To <span>Brisa Lagoon</span></h1>
</header>

<section>
  <div class="abs hero" role="img" aria-label="Friends laughing with drinks in a sunny pool"></div>
  <div class="abs hero-bar">
    <svg width="12" height="16" viewBox="0 0 12 16"><path d="M9 2 3 8l6 6" fill="none" stroke="#222" stroke-width="2.5"/></svg>
    <span class="dot"></span><span class="dot on"></span><span class="dot"></span><span class="dot"></span>
    <svg width="12" height="16" viewBox="0 0 12 16"><path d="m3 2 6 6-6 6" fill="none" stroke="#222" stroke-width="2.5"/></svg>
  </div>
</section>

<section>
  <div class="abs tile blue" style="left:111px;top:770px;width:603px;height:370px;padding-top:58px;padding-right:48px">
    <h2>Personalized Services</h2>
    <p>We understand that every garden and client is unique. That's why we offer personalized services, from design to installation and after-sales support. Our team of experts is here to answer all your questions and guide you throughout your project.</p>
  </div>
  <div class="abs" style="left:714px;top:770px;width:375px;height:370px;background:linear-gradient(160deg,#2aa7e0,#0c6fb8 60%,#3cb6e8)" role="img" aria-label="Children swimming underwater in goggles"></div>
  <div class="abs" style="left:111px;top:1142px;width:603px;height:470px;background:linear-gradient(120deg,#48c4ea,#1fa6dc 60%,#5aa63a)" role="img" aria-label="Child floating on a sprinkled ring in an above-ground pool"></div>
  <div class="abs tile green" style="left:714px;top:1142px;width:375px;height:470px;padding-top:28px;padding-left:46px;padding-right:56px">
    <h2>Guaranteed Satisfaction</h2>
    <p>Your satisfaction is our top priority. We are committed to providing you with exceptional service and the highest quality products. Join our community of satisfied customers who are already enjoying their custom above-ground pools. 10-Year Warranty!</p>
  </div>
</section>

<section class="abs why">
  <h2>Why Choose<br>Our Above-Ground Pools?</h2>
  <div class="abs card" style="left:111px;top:260px">
    <div class="pic" role="img" aria-label="Poolside loungers and parasols with star rating" style="background:linear-gradient(180deg,#8fb8e0,#c9dcee 55%,#4fb7e3)"></div>
    <div class="label">Superior Quality <svg width="28" height="14" viewBox="0 0 28 14"><path d="M0 7h24M18 1l7 6-7 6" fill="none" stroke="#fff" stroke-width="2.5"/></svg></div>
  </div>
  <div class="abs card" style="left:611px;top:260px">
    <div class="pic" role="img" aria-label="Modern pool house with lit pool at dusk" style="background:linear-gradient(180deg,#5c8fc4,#d8dde0 45%,#1b5f82)"></div>
    <div class="label">Elegant Design <svg width="28" height="14" viewBox="0 0 28 14"><path d="M0 7h24M18 1l7 6-7 6" fill="none" stroke="#fff" stroke-width="2.5"/></svg></div>
  </div>
  <div class="abs card" style="left:111px;top:716px">
    <div class="pic" role="img" aria-label="Tailor-made pool beside an open villa lounge" style="background:linear-gradient(180deg,#6e8a5a,#a89a86 45%,#5aa8a8)"></div>
    <div class="label">Custom and Tailor-Made <svg width="28" height="14" viewBox="0 0 28 14"><path d="M0 7h24M18 1l7 6-7 6" fill="none" stroke="#fff" stroke-width="2.5"/></svg></div>
  </div>
  <div class="abs card" style="left:611px;top:716px">
    <div class="pic" role="img" aria-label="Coiled pool hose floating in blue water" style="background:linear-gradient(160deg,#0d5c8e,#26a6dc 50%,#0b4f80)"></div>
    <div class="label">Easy Installation <svg width="28" height="14" viewBox="0 0 28 14"><path d="M0 7h24M18 1l7 6-7 6" fill="none" stroke="#fff" stroke-width="2.5"/></svg></div>
  </div>
  <div class="abs card" style="left:361px;top:1155px">
    <div class="pic" role="img" aria-label="Swimmer gliding through rippling blue water" style="background:linear-gradient(150deg,#1b8fd0,#55c3ea 50%,#1778bf)"></div>
    <div class="label">Constant Innovation <svg width="28" height="14" viewBox="0 0 28 14"><path d="M0 7h24M18 1l7 6-7 6" fill="none" stroke="#fff" stroke-width="2.5"/></svg></div>
  </div>
</section>

<section>
  <div class="abs" style="left:111px;top:3510px;width:375px;height:562px;background:linear-gradient(170deg,#7fd3e6,#e2c3a8 45%,#6cc7c8 75%,#4fb0b4)" role="img" aria-label="Woman in a sun hat relaxing at the pool edge"></div>
  <div class="abs tile blue" style="left:486px;top:3510px;width:603px;height:562px;padding-top:32px;padding-left:51px;padding-right:48px">
    <h2 style="line-height:1.32;margin-bottom:36px">Transform Your Garden<br>with Our Premium<br>Above-Ground Pools!</h2>
    <p style="margin-bottom:28px">Achieve your dreams with our custom, tailor-made above-ground pools.</p>
    <p>Imagine an exceptional relaxation and leisure space right in your own backyard. With our unparalleled expertise and commitment to excellence, we create above-ground pools that exceed all expectations. Our exclusive, custom-designed models are crafted to combine style, durability, and innovation, offering a unique and refined experience.</p>
  </div>
  <div class="abs tile green" style="left:111px;top:4074px;width:603px;height:412px;padding-top:56px;padding-left:42px;padding-right:60px">
    <h2>Contact Us Today</h2>
    <p>Don't wait any longer to transform your garden into a wellness oasis. Contact us today to discover our range of customizable above-ground pools and get a tailored quote. Dive into a world of infinite possibilities with [Your Company Name].</p>
    <span class="btn">We Bring Your Pool Dreams to Life!</span>
  </div>
  <div class="abs" style="left:714px;top:4074px;width:375px;height:412px;background:linear-gradient(135deg,#a9cde3,#e8efef 45%,#7cc8bf 75%,#2f8a78)" role="img" aria-label="Striped beach cabana against a clear sky"></div>
</section>

<footer class="abs footer">
  <div class="brand-foot">Brisa Lagoon</div>
  <div class="subscribe">Subscribe to our emails</div>
  <div class="email"><span>Email</span>
    <svg width="26" height="14" viewBox="0 0 26 14"><path d="M0 7h22M16 1l7 6-7 6" fill="none" stroke="#fff" stroke-width="2.5"/></svg>
  </div>
  <div class="rule"></div>
  <div class="copy">© 2024 Brisa Lagoon . All Rights Reserved</div>
</footer>

</body>
</html>
```